Global (re)insurance broker needs a business card design

We need a classic business card for our company that is headquartered in SG, with offices in Portugal and Qatar. We specialise in insurance and reinsurance broking and consultancy for our global clients.

```html
<!DOCTYPE html>
<html lang="en">
<head>
<meta charset="utf-8">
<title>Velmare Business Card</title>
<link href="https://fonts.googleapis.com/css2?family=Poppins:wght@400;500;600&display=swap" rel="stylesheet">
<style>
  :root {
    --backdrop: #2b2b2c;
    --card: #1c1d1f;
    --brand-blue: #2c4aa3;
    --brand-green: #c9e5bd;
    --text-light: #f2f2f2;
    --rule: #8a8a8a;
    --pattern-dark: #17181a;
    --pattern-light: #2a2b2e;
  }
  * { margin: 0; padding: 0; box-sizing: border-box; }
  html, body {
    width: 1200px; height: 1108px; overflow: hidden;
    background: var(--backdrop);
    font-family: "Poppins", sans-serif;
  }
  .canvas {
    width: 1200px; height: 1108px;
    display: flex; align-items: center; justify-content: center; gap: 80px;
  }
  .card {
    width: 400px; height: 660px;
    background: var(--card);
    border-radius: 18px;
    position: relative;
    overflow: hidden;
    box-shadow: 0 20px 40px rgba(0,0,0,.45);
  }
  .card-front {
    display: flex; flex-direction: column; align-items: center;
    padding: 120px 40px 0;
  }
  .brand-name {
    font-weight: 600; font-size: 64px; letter-spacing: 2px;
    color: var(--brand-green); line-height: 1;
  }
  .person { margin-top: 170px; text-align: center; }
  .person-name { font-weight: 600; font-size: 26px; letter-spacing: 1px; line-height: 1.1; }
  .person-name .first { color: var(--brand-blue); }
  .person-name .last { color: var(--brand-green); }
  .person-role { font-size: 16px; color: var(--text-light); letter-spacing: .5px; margin-top: 2px; }
  .icon-row {
    display: flex; align-items: center; gap: 8px; width: 290px; margin-top: 18px;
  }
  .icon-row .rule { flex: 1; height: 1px; background: var(--rule); }
  .icon-box {
    width: 28px; height: 28px; border-radius: 4px; background: var(--brand-blue);
    display: flex; align-items: center; justify-content: center;
  }
  .contact { margin-top: 12px; text-align: center; color: var(--text-light); font-size: 17px; line-height: 1.45; }
  .divider { width: 290px; height: 1px; background: var(--rule); margin-top: 14px; }
  .location { margin-top: 14px; color: var(--text-light); font-size: 16px; }
  .card-back { display: flex; align-items: center; justify-content: center; }
  .back-pattern {
    position: absolute; inset: 0;
    background: linear-gradient(135deg, var(--pattern-dark) 0%, var(--pattern-light) 50%, var(--pattern-dark) 100%);
  }
  .back-brand {
    position: relative; font-weight: 600; font-size: 34px; letter-spacing: 1.5px;
    color: var(--brand-green);
  }
</style>
</head>
<body>
<main class="canvas">
  <section class="card card-front">
    <div class="brand-name">VELMARE</div>
    <div class="person">
      <div class="person-name"><span class="first">ADRIAN</span> <span class="last">COLE</span></div>
      <div class="person-role">MANAGING DIRECTOR</div>
    </div>
    <div class="icon-row">
      <span class="rule"></span>
      <span class="icon-box" aria-label="Phone">
        <svg width="16" height="16" viewBox="0 0 24 24"><path fill="#1c1d1f" d="M6.6 10.8a15 15 0 0 0 6.6 6.6l2.2-2.2a1 1 0 0 1 1-.25 11.4 11.4 0 0 0 3.6.57 1 1 0 0 1 1 1V20a1 1 0 0 1-1 1A17 17 0 0 1 3 4a1 1 0 0 1 1-1h3.5a1 1 0 0 1 1 1c0 1.25.2 2.450.57 3.57a1 1 0 0 1-.25 1z"/></svg>
      </span>
      <span class="icon-box" aria-label="Email">
        <svg width="16" height="16" viewBox="0 0 24 24"><rect x="3" y="6" width="18" height="12" rx="1" fill="none" stroke="#1c1d1f" stroke-width="2"/><path d="M3 7l9 6 9-6" fill="none" stroke="#1c1d1f" stroke-width="2"/></svg>
      </span>
      <span class="icon-box" aria-label="Website">
        <svg width="16" height="16" viewBox="0 0 24 24"><circle cx="12" cy="12" r="9" fill="none" stroke="#1c1d1f" stroke-width="2"/><path d="M3 12h18M12 3c3 3 3 15 0 18M12 3c-3 3-3 15 0 18" fill="none" stroke="#1c1d1f" stroke-width="1.5"/></svg>
      </span>
      <span class="rule"></span>
    </div>
    <div class="contact">
      <div>065-987 321 450</div>
      <div>hello@velmare.com</div>
      <div>www.velmare.com</div>
    </div>
    <div class="divider"></div>
    <div class="location">Portugal and Qatar</div>
  </section>
  <section class="card card-back">
    <div class="back-pattern" role="img" aria-label="Repeating gloss brand-name pattern across the card back"></div>
    <div class="back-brand">VELMARE</div>
  </section>
</main>
</body>
</html>
```